House-share and Room Rental Website (With Focus on the Bedroom Landing Page)

Looking for website design for our House-share (executive accommodation) and room rental business.

Our company name is: Lodvenra could also be written as LodVenra or lodvenra. Either is fine .. just looking for a nice clean catchy logo to go with the design.

EXAMPLES
These are examples of other websites in this field that are doing well. this is a kind of baseline.
https://kelbrin.com.au/
https://www.tuvaplex.com/
https://www.nestorvi.com/
https://www.quillsa.net/
https://www.pendlebarrow.com.au/

Our business model is to rent rooms to people looking for high-quality accommodation. We fill the gap between those looking to rent rooms and those with rooms to rent. However, our model is slightly different from those already on the market as we looking to fill a massive gap in the market delivering upmarket rooms for rent.(Executive Accommodation) also in the back end will be coupled with a self management process in the back end.

We offer executive style accommodation that stands out above the rest. With special extras like fire safety.. and management processes that create happier homes. We are looking for a web design package that can help us grow and scale our business. We need a design that is captivating

Our MAIN focus is having a room landing page that stands out from the rest... The core of our business will rely on the promotion of the rooms in a share house... so the whole design relies on the BEDROOM landing page to drive results.

Target Market(s)

We have 2 markets we are aiming at ... the first market is people offering rooms to rent who want the highest rental return. The second market is people looking to rent safe, high-quality rooms, in houses that are well managed and looked after.

Industry/Entity Type

Share Economy

Logo Text

LodVenra

Number of Pages Required

5+ page

Font styles to use
Sans Serif

Colors
3276b5

Requirements
Must have
• A messaging system whereby we can create direct communication between those offering rooms and those looking for rooms.
• A call to action that says " Schedule an Inspection"
• Landing page for promoting rooms
• A home page for showing stock.
• Profile page for those selling rooms
• Profile page for those looking for rooms.
• A scheduling calendar for booking inspections
Nice to have
• Pages where new residents can lock in a room.. pay bond and rents.. and sign contracts
• Notifications
• SMS capabilities in the backend.
Should not have
• No script or handwriting fonts.

```html
<!DOCTYPE html>
<html lang="en">
<head>
<meta charset="utf-8">
<title>Lodvenra – Newest Bedroom</title>
<link href="https://fonts.googleapis.com/css2?family=Montserrat:wght@600;700&family=Lato:wght@400;700&family=Open+Sans:wght@400&family=Roboto+Condensed:wght@700&display=swap" rel="stylesheet">
<style>
  :root{
    --brand:#0a9be0;
    --ink:#2d2d2d;
    --muted:#8a8a8a;
    --card-bg:#f8f9fb;
    --feature-bg:#f3f4f7;
    --rent:#4caf50;
    --share:#f5a623;
    --tag:#2f2f2f;
    --pink:#f58b8b;
    --chat-bg:#ececec;
    --bubble-in:#c6c6cc;
    --bubble-out:#52b5f0;
    --white:#ffffff;
  }
  *{box-sizing:border-box;margin:0;padding:0}
  html,body{width:1200px;height:1200px;overflow:hidden;background:var(--white)}
  body{position:relative;font-family:'Lato',sans-serif;color:var(--ink)}

  .services{position:absolute;left:0;top:0;width:1200px;height:179px;background:var(--brand);overflow:hidden}
  .service{position:absolute;top:0;width:300px;text-align:center;color:var(--white)}
  .service-ring{position:absolute;left:50%;top:-58px;width:84px;height:84px;margin-left:-42px;border:4px solid var(--white);border-radius:50%}
  .service-title{position:absolute;left:0;right:0;top:41px;font-family:'Montserrat',sans-serif;font-weight:700;font-size:16px}
  .service-text{position:absolute;left:0;right:0;top:72px;font-size:11.5px;line-height:21px}

  .section-head{position:absolute;left:0;width:1200px;top:249px;text-align:center}
  .section-title{font-family:'Lato',sans-serif;font-weight:700;font-size:22px;letter-spacing:-.3px;color:#333}
  .section-sub{margin-top:6px;font-family:'Open Sans',sans-serif;font-size:12px;color:var(--muted);letter-spacing:.3px}

  .card{position:absolute;background:var(--card-bg)}
  .card-photo{position:absolute;left:0;top:0;width:100%}
  .badge{position:absolute;top:14px;right:14px;padding:4px 9px;font-size:7.5px;font-weight:700;color:var(--white);letter-spacing:.1px}
  .badge.rent{background:var(--rent)}
  .badge.share{background:var(--share)}
  .price{position:absolute;left:12px;height:31px;padding:0 13px;line-height:31px;background:var(--tag);color:var(--white);font-weight:700;font-size:12px;border-radius:3px}
  .address{position:absolute;left:22px;font-size:8px;color:#333;display:flex;align-items:center;gap:5px;text-transform:uppercase;white-space:nowrap}
  .listing-title{position:absolute;left:22px;font-family:'Montserrat',sans-serif;font-weight:600;font-size:15px;color:#2d2d2d;white-space:nowrap}
  .features{position:absolute;left:0;right:0;height:34px;background:var(--feature-bg);display:flex;align-items:center;gap:13px;padding-left:22px;font-size:9px;color:#9a9a9a;white-space:nowrap}
  .feature{display:flex;align-items:center;gap:4px}

  .inspect{position:absolute;left:527px;top:1102px;width:146px;height:39px}
  .inspect span{position:absolute;left:0;right:0;top:23px;text-align:center;font-family:'Roboto Condensed',sans-serif;font-weight:700;font-size:12px;color:var(--white);letter-spacing:-.2px;white-space:nowrap}
  .view-all{position:absolute;left:519px;top:1162px;width:171px;height:44px;border-radius:22px;background:var(--brand);color:var(--white);font-family:'Roboto Condensed',sans-serif;font-weight:700;font-size:18px;text-align:center;line-height:40px}

  .chat{position:absolute;left:837px;top:699px;width:347px;height:501px;background:var(--white);z-index:5}
  .chat-head{height:64px;background:var(--brand);color:var(--white);position:relative}
  .chat-title{position:absolute;left:18px;top:18px;font-family:'Roboto Condensed',sans-serif;font-weight:700;font-size:21px;white-space:nowrap}
  .chat-body{position:absolute;top:64px;left:0;width:347px;height:311px;background:var(--chat-bg)}
  .chat-scroll{position:absolute;right:9px;top:11px;width:7px;height:290px;border-radius:4px;background:#f7f7f7}
  .chat-scroll i{position:absolute;left:0;top:0;width:7px;height:193px;border-radius:4px;background:var(--brand)}
  .bubble{position:absolute;font-size:13.5px;padding:0 13px;height:40px;line-height:40px;border-radius:3px;white-space:nowrap}
  .bubble.in{left:20px;background:var(--bubble-in);color:#222}
  .bubble.out{right:34px;background:var(--bubble-out);color:var(--white)}
  .chat-tools{position:absolute;left:23px;top:386px;display:flex;gap:8px}
  .chat-input{position:absolute;left:15px;top:415px;width:319px;height:62px;border:1.5px solid #cfcfcf;border-radius:3px;background:var(--white)}
  .chat-input span{position:absolute;left:13px;top:22px;font-size:12px;font-style:italic;color:#8a8a8a;white-space:nowrap}
  .chat-send{position:absolute;right:4px;top:5px;width:45px;height:51px;background:#1e88e5;border:1.5px solid #1565c0;border-radius:4px}
</style>
</head>
<body>

<section class="services">
  <div class="service" style="left:154px"><div class="service-ring"></div><div class="service-title">Modern Rooms</div><div class="service-text">Vestibulum at magna tellus. Vivamus is<br>amus porta ligula in orc</div></div>
  <div class="service" style="left:462px"><div class="service-ring"></div><div class="service-title">Fire Protection Services</div><div class="service-text">Vestibulum at magna tellus. Vivamus is<br>amus porta ligula in orc</div></div>
  <div class="service" style="left:756px"><div class="service-ring"></div><div class="service-title">Child Rooms</div><div class="service-text">We have design comfortable child rooms<br>for your childrens</div></div>
</section>

<header class="section-head">
  <h2 class="section-title">Newest Bedroom</h2>
  <p class="section-sub">Absolutely Stunning Design and Functionality</p>
</header>

<article class="card" style="left:160px;top:338px;width:429px;height:436px">
  <div class="card-photo" role="img" aria-label="Warm bedroom with a large bed, golden walls and a sitting area" style="height:320px;background:linear-gradient(135deg,#5a4535 0%,#b08552 45%,#e2b57a 70%,#6d5a44 100%)"></div>
  <span class="badge rent">FOR RENT</span>
  <div class="price" style="top:280px">$625,000</div>
  <div class="address" style="top:343px"><svg width="7" height="10" viewBox="0 0 7 10"><path d="M3.5 0C1.6 0 0 1.5 0 3.4 0 6 3.5 10 3.5 10S7 6 7 3.4C7 1.5 5.4 0 3.5 0z" fill="#333"/><circle cx="3.5" cy="3.4" r="1.3" fill="#fff"/></svg>42 Marlow Lane, Ferndale, NY 10377, USA</div>
  <div class="listing-title" style="top:363px">Small cottage in Upper New</div>
  <div class="features" style="top:402px">
    <span class="feature"><svg width="15" height="9"><rect x="0" y="0" width="2" height="9" fill="#aaa"/><rect x="0" y="5" width="15" height="2" fill="#aaa"/><rect x="5" y="2" width="10" height="3" fill="#aaa"/></svg>4 Beds</span>
    <span class="feature"><svg width="15" height="9"><path d="M0 2h15v2c0 3-2 5-5 5H5C2 9 0 7 0 4z" fill="#aaa"/></svg>3 Bath</span>
    <span class="feature"><svg width="8" height="11" viewBox="0 0 7 10"><path d="M3.5 0C1.6 0 0 1.5 0 3.4 0 6 3.5 10 3.5 10S7 6 7 3.4C7 1.5 5.4 0 3.5 0z" fill="#aaa"/></svg>250m²</span>
    <span class="feature"><svg width="14" height="10"><path d="M1 4L7 0l6 4v6H1z" fill="none" stroke="#aaa" stroke-width="1.4"/></svg>2 Garages</span>
  </div>
</article>

<article class="card" style="left:610px;top:338px;width:429px;height:436px">
  <div class="card-photo" role="img" aria-label="Modern bedroom with a grey bed, teal accents and a lounge chair" style="height:320px;background:linear-gradient(135deg,#c8cfd3 0%,#e6eaec 40%,#9fc8cf 60%,#d9dcde 100%)"></div>
  <span class="badge rent">FOR RENT</span>
  <div class="price" style="top:280px">$625,000</div>
  <div class="address" style="top:343px"><svg width="7" height="10" viewBox="0 0 7 10"><path d="M3.5 0C1.6 0 0 1.5 0 3.4 0 6 3.5 10 3.5 10S7 6 7 3.4C7 1.5 5.4 0 3.5 0z" fill="#333"/><circle cx="3.5" cy="3.4" r="1.3" fill="#fff"/></svg>42 Marlow Lane, Ferndale, NY 10377, USA</div>
  <div class="listing-title" style="top:363px">Small cottage in Upper New</div>
  <div class="features" style="top:402px">
    <span class="feature"><svg width="15" height="9"><rect x="0" y="0" width="2" height="9" fill="#aaa"/><rect x="0" y="5" width="15" height="2" fill="#aaa"/><rect x="5" y="2" width="10" height="3" fill="#aaa"/></svg>4 Beds</span>
    <span class="feature"><svg width="15" height="9"><path d="M0 2h15v2c0 3-2 5-5 5H5C2 9 0 7 0 4z" fill="#aaa"/></svg>3 Bath</span>
    <span class="feature"><svg width="8" height="11" viewBox="0 0 7 10"><path d="M3.5 0C1.6 0 0 1.5 0 3.4 0 6 3.5 10 3.5 10S7 6 7 3.4C7 1.5 5.4 0 3.5 0z" fill="#aaa"/></svg>250m²</span>
    <span class="feature"><svg width="14" height="10"><path d="M1 4L7 0l6 4v6H1z" fill="none" stroke="#aaa" stroke-width="1.4"/></svg>2 Garages</span>
  </div>
</article>

<article class="card" style="left:162px;top:798px;width:277px;height:294px">
  <div class="card-photo" role="img" aria-label="Dark contemporary bedroom with a low bed and wardrobe" style="height:178px;background:linear-gradient(135deg,#2f2f33 0%,#55524f 50%,#8b8580 80%,#e3e0dc 100%)"></div>
  <span class="badge share">FOR SHARE</span>
  <div class="price" style="top:140px">$625,000</div>
  <div class="address" style="top:201px"><svg width="7" height="10" viewBox="0 0 7 10"><path d="M3.5 0C1.6 0 0 1.5 0 3.4 0 6 3.5 10 3.5 10S7 6 7 3.4C7 1.5 5.4 0 3.5 0z" fill="#333"/><circle cx="3.5" cy="3.4" r="1.3" fill="#fff"/></svg>Galtur ( Austria )</div>
  <div class="listing-title" style="top:222px">Villa On Washington Ave</div>
  <div class="features" style="top:260px">
    <span class="feature"><svg width="15" height="9"><rect x="0" y="0" width="2" height="9" fill="#aaa"/><rect x="0" y="5" width="15" height="2" fill="#aaa"/><rect x="5" y="2" width="10" height="3" fill="#aaa"/></svg>4 Beds</span>
    <span class="feature"><svg width="15" height="9"><path d="M0 2h15v2c0 3-2 5-5 5H5C2 9 0 7 0 4z" fill="#aaa"/></svg>3 Bath</span>
    <span class="feature"><svg width="8" height="11" viewBox="0 0 7 10"><path d="M3.5 0C1.6 0 0 1.5 0 3.4 0 6 3.5 10 3.5 10S7 6 7 3.4C7 1.5 5.4 0 3.5 0z" fill="#aaa"/></svg>250m²</span>
    <span class="feature"><svg width="14" height="10"><path d="M1 4L7 0l6 4v6H1z" fill="none" stroke="#aaa" stroke-width="1.4"/></svg>2 Garages</span>
  </div>
</article>

<article class="card" style="left:462px;top:798px;width:277px;height:294px">
  <div class="card-photo" role="img" aria-label="Bright bedroom with a white bed and tall windows overlooking a harbour" style="height:178px;background:linear-gradient(135deg,#b9c3cc 0%,#e4e8ec 45%,#c9ced2 70%,#8e9aa4 100%)"></div>
  <span class="badge rent">FOR RENT</span>
  <div class="price" style="top:140px">$625,000</div>
  <div class="address" style="top:201px"><svg width="7" height="10" viewBox="0 0 7 10"><path d="M3.5 0C1.6 0 0 1.5 0 3.4 0 6 3.5 10 3.5 10S7 6 7 3.4C7 1.5 5.4 0 3.5 0z" fill="#333"/><circle cx="3.5" cy="3.4" r="1.3" fill="#fff"/></svg>Galtur ( Austria )</div>
  <div class="listing-title" style="top:222px">Villa On Washington Ave</div>
  <div class="features" style="top:260px">
    <span class="feature"><svg width="15" height="9"><rect x="0" y="0" width="2" height="9" fill="#aaa"/><rect x="0" y="5" width="15" height="2" fill="#aaa"/><rect x="5" y="2" width="10" height="3" fill="#aaa"/></svg>4 Beds</span>
    <span class="feature"><svg width="15" height="9"><path d="M0 2h15v2c0 3-2 5-5 5H5C2 9 0 7 0 4z" fill="#aaa"/></svg>3 Bath</span>
    <span class="feature"><svg width="8" height="11" viewBox="0 0 7 10"><path d="M3.5 0C1.6 0 0 1.5 0 3.4 0 6 3.5 10 3.5 10S7 6 7 3.4C7 1.5 5.4 0 3.5 0z" fill="#aaa"/></svg>250m²</span>
    <span class="feature"><svg width="14" height="10"><path d="M1 4L7 0l6 4v6H1z" fill="none" stroke="#aaa" stroke-width="1.4"/></svg>2 Garages</span>
  </div>
</article>

<article class="card" style="left:762px;top:798px;width:277px;height:294px">
  <div class="card-photo" role="img" aria-label="Bedroom with warm wood tones and a colourful shelf" style="height:178px;background:linear-gradient(135deg,#6b3a2a 0%,#a5684b 50%,#d99b8f 100%)"></div>
  <div class="price" style="top:140px">$625,000</div>
  <div class="address" style="top:201px"><svg width="7" height="10" viewBox="0 0 7 10"><path d="M3.5 0C1.6 0 0 1.5 0 3.4 0 6 3.5 10 3.5 10S7 6 7 3.4C7 1.5 5.4 0 3.5 0z" fill="#333"/><circle cx="3.5" cy="3.4" r="1.3" fill="#fff"/></svg>Galtur ( Austria )</div>
  <div class="listing-title" style="top:222px">Villa On Washington Ave</div>
  <div class="features" style="top:260px">
    <span class="feature"><svg width="15" height="9"><rect x="0" y="0" width="2" height="9" fill="#aaa"/><rect x="0" y="5" width="15" height="2" fill="#aaa"/><rect x="5" y="2" width="10" height="3" fill="#aaa"/></svg>4 Beds</span>
  </div>
</article>

<a class="inspect">
  <svg width="146" height="39" viewBox="0 0 146 39"><path d="M0 18 L73 0 L146 18 V39 H0 Z" fill="var(--pink)"/></svg>
  <span>SCHEDULE AN INSPECTION</span>
</a>
<a class="view-all">VIEW ALL ROOMS</a>

<aside class="chat">
  <div class="chat-head">
    <div class="chat-title">Lodvenra Could Live Chat</div>
    <svg style="position:absolute;left:276px;top:20px" width="60" height="24"><line x1="0" y1="22" x2="22" y2="22" stroke="#fff" stroke-width="2"/><path d="M40 2l18 18M58 2L40 20" stroke="#fff" stroke-width="2.2"/></svg>
  </div>
  <div class="chat-body">
    <svg style="position:absolute;left:28px;top:34px" width="10" height="10"><path d="M0 0v10h10z" fill="var(--bubble-in)"/></svg>
    <div class="bubble in" style="top:43px">Hi!</div>
    <div class="bubble in" style="top:96px">How may I help you?</div>
    <div class="bubble out" style="top:148px">Hello!</div>
    <svg style="position:absolute;left:296px;top:188px" width="8" height="9"><path d="M0 0h8L4 9z" fill="var(--bubble-out)"/></svg>
    <div class="bubble out" style="top:204px">I need help with the design.</div>
    <div class="chat-scroll"><i></i></div>
  </div>
  <div class="chat-tools">
    <svg width="20" height="18" viewBox="0 0 20 18"><path d="M0 6h4l5-5v16l-5-5H0z" fill="#555"/><path d="M12 5c2 2 2 6 0 8M15 3c3 3 3 9 0 12" stroke="#555" stroke-width="1.5" fill="none"/></svg>
    <svg width="14" height="20" viewBox="0 0 14 20"><rect x="4" y="0" width="6" height="12" rx="3" fill="#555"/><path d="M1 9c0 4 3 6 6 6s6-2 6-6M7 15v5" stroke="#555" stroke-width="1.6" fill="none"/></svg>
  </div>
  <div class="chat-input">
    <span>Type your message here...</span>
    <div class="chat-send"><svg width="45" height="51" viewBox="0 0 45 51"><path d="M8 16l30 9.5L8 35l6-9.5z" fill="#fff"/></svg></div>
  </div>
</aside>

</body>
</html>
```